Business Card for Marriage Commissioner

I am a marriage commissioner in the province of Alberta, meaning that I perform civil unions here. I have been trying to think of a unique design for my business card, something a bit different. A lot of "unique" designs seem to incorporate unique cuts or "some assembly required" or printed on plastic or meat. I would like my design to be a full colour card that is a typical business card size.

The information on the card should have:
Lou Varnik
my occupation: Marriage Commissioner
my website: www.louvarnik.ca
my e-mail: lou@louvarnik.ca
my phone: 780-418-2964

I originally submitted a design to the printer that had a screen capture of a findly search window, with my name and occupation in the text box. And underneath that, my phone number. Nothing else. They indicated they could not print this because it was a copyright violation.

One option on the design is I am a retired chemist-so a chemistry themed card would also be of interest, as long as it isn't a "Rusted Tide" theme, as I have that on my other business cards already...

I would prefer a single sided card, but I am open to a double sided card if it is clever!

I would also prefer not to have pictures of male and female couples as in my position I will also marry same sex couples. Same thing for male/female symbols. Someone has submitted two graduated cylinders in love, which is very clever, and gets around this male/female type.

Thanks for your help and interest.

Target Market(s)

Young couples.

Industry/Entity Type

Plastic

Requirements
Nice to have
• chemistry ideas!
Should not have
• Male/female pictures, male/female symbols.
No QR codes.
No transparent designs, will go on paper stock.

```html
<!DOCTYPE html>
<html lang="en">
<head>
<meta charset="utf-8">
<title>Lou Varnik – Marriage Commissioner</title>
<link rel="stylesheet" href="https://fonts.googleapis.com/css2?family=Yellowtail&family=Lato:wght@400;700&display=swap">
<style>
  :root {
    --page-bg: #f6f6f6;
    --card-bg: #ffffff;
    --teal: #93c4cc;
    --grey: #939393;
    --ring: #959595;
    --white: #ffffff;
  }
  * { margin: 0; padding: 0; box-sizing: border-box; }
  html, body {
    width: 1200px;
    height: 900px;
    overflow: hidden;
    background: var(--page-bg);
  }
  .business-card {
    position: absolute;
    left: 75px;
    top: 150px;
    width: 1050px;
    height: 600px;
    background: var(--card-bg);
    box-shadow: 1px 2px 4px rgba(0,0,0,0.28);
  }
  .accent-band {
    position: absolute;
    left: 0;
    top: 251px;
    width: 100%;
    height: 59px;
    background: var(--teal);
  }
  .portrait {
    position: absolute;
    left: 144px;
    top: 167px;
    width: 226px;
    height: 226px;
  }
  .holder-name {
    position: absolute;
    left: 428px;
    top: 130px;
    font-family: "Yellowtail", cursive;
    font-size: 112px;
    line-height: 1;
    color: var(--grey);
    white-space: nowrap;
  }
  .occupation {
    position: absolute;
    left: 439px;
    top: 256px;
    font-family: "Lato", sans-serif;
    font-size: 21px;
    color: var(--white);
    letter-spacing: 0.2px;
  }
  .contact {
    position: absolute;
    right: 78px;
    top: 435px;
    text-align: right;
    font-family: "Lato", sans-serif;
    font-weight: 700;
    color: var(--grey);
  }
  .contact .phone {
    color: var(--teal);
    font-size: 30px;
    letter-spacing: 1px;
    line-height: 40px;
  }
  .contact .email,
  .contact .website {
    font-size: 26px;
    line-height: 38px;
  }
  .tagline {
    position: absolute;
    left: 83px;
    top: 510px;
    font-family: "Yellowtail", cursive;
    font-size: 22px;
    color: var(--teal);
    white-space: nowrap;
  }
</style>
</head>
<body>
  <article class="business-card">
    <div class="accent-band"></div>

    <svg class="portrait" viewBox="0 0 226 226" role="img" aria-label="Portrait photo of the marriage commissioner">
      <defs>
        <radialGradient id="portrait-tone" cx="45%" cy="45%" r="60%">
          <stop offset="0%" stop-color="#e3b79c"/>
          <stop offset="60%" stop-color="#c9977c"/>
          <stop offset="100%" stop-color="#f4eeea"/>
        </radialGradient>
      </defs>
      <circle cx="113" cy="113" r="109" fill="url(#portrait-tone)" stroke="var(--ring)" stroke-width="8"/>
    </svg>

    <h1 class="holder-name">Lou Varnik</h1>
    <p class="occupation">Marriage Commissioner</p>

    <div class="contact">
      <p class="phone">780-418-2964</p>
      <p class="email">lou@louvarnik.ca</p>
      <p class="website">www.louvarnik.ca</p>
    </div>

    <p class="tagline">Marriage ceremonies for committed couples</p>
  </article>
</body>
</html>
```